High value cover design for an A4 ideation pad.

The product is NOT A BOOK.

It's an A4 ideation pad for professionals, designers and creators who handwrite their ideas. Visualise creators like Paul Menteith, Glen Usborne and Carl Whitmoor in your mind's eye.

I'm looking for a cover design for the ideation pad. Both front and back.

It should look, feel and convey the following.

--> A handcrafted product experience

--> High value & Elegance

--> Inspiration

Mandatory --> See Uploaded Files --> Files 1, 5 & 6

Target Market(s)

- Designers

-Creative Professionals

- Entrepreneurs

who handwrite their ideas. Visualise creators like Paul Menteith, Glen Usborne and Carl Whitmoor in your mind's eye.

Industry/Entity Type

Stationary

Font styles to use
Script
Other font styles liked:
• Calligraphy

Colors
fbed22

Requirements
Must have
• Title text - Ink And Iron

-Text in gold on brown leather background to convey high value for the front cover.

--> High value & Elegance

--> Inspiration

--> Should compel the customers to pick up and own the idea pad
Nice to have
• That's my take but other ideas are welcome
Should not have
• Must not convey

- low value

```html
<!DOCTYPE html>
<html lang="en">
<head>
<meta charset="utf-8">
<title>Ink And Iron — Ideation Pad Cover</title>
<link rel="stylesheet" href="https://fonts.googleapis.com/css2?family=Great+Vibes&display=swap">
<style>
  :root {
    --canvas: #ededed;
    --leather: #9d4a1d;
    --leather-light: #a9552a;
    --leather-dark: #8a3f17;
    --gold-light: #fbed22;
    --gold: #e0b43a;
    --gold-deep: #b47f1a;
  }
  * { margin: 0; padding: 0; box-sizing: border-box; }
  html, body {
    width: 1200px;
    height: 1200px;
    overflow: hidden;
    background: var(--canvas);
  }
  .spread {
    position: relative;
    width: 1200px;
    height: 1200px;
  }
  .cover {
    position: absolute;
    top: 328px;
    width: 417px;
    height: 568px;
    background:
      radial-gradient(ellipse at 40% 35%, var(--leather-light) 0%, var(--leather) 55%, var(--leather-dark) 100%);
  }
  .cover--front { left: 99px; }
  .cover--back { left: 684px; }
  .gold-frame {
    position: absolute;
    inset: 8px 8px 9px 9px;
    border: 3px solid var(--gold);
    border-image: linear-gradient(135deg, var(--gold-deep), var(--gold-light) 45%, var(--gold) 70%, var(--gold-deep)) 1;
  }
  .title {
    position: absolute;
    left: 0;
    right: 0;
    text-align: center;
    font-family: "Great Vibes", cursive;
    font-weight: 400;
    background: linear-gradient(135deg, var(--gold-deep) 0%, var(--gold-light) 45%, var(--gold) 65%, var(--gold-deep) 100%);
    -webkit-background-clip: text;
    background-clip: text;
    color: transparent;
    line-height: 1;
  }
  .title__lead {
    top: 80px;
    font-size: 56px;
    letter-spacing: 2px;
  }
  .title__main {
    top: 190px;
    font-size: 150px;
  }
</style>
</head>
<body>
  <main class="spread">
    <section class="cover cover--front" aria-label="Front cover">
      <div class="gold-frame"></div>
      <h1>
        <span class="title title__lead">Ink And</span>
        <span class="title title__main">Iron</span>
      </h1>
    </section>
    <section class="cover cover--back" aria-label="Back cover"></section>
  </main>
</body>
</html>
```